Business Card Design Project

We need a business card for our IT services provider business. We provide services to small and medium business, and would like something that reflects the color scheme / branding on our recently updated website - www.tallobrix.com.au

The card type we have chosen is a matte laminated double sided configuration at 86mm x 54mm on 350 GSM cardboard.
Updates

Target Market(s)

Small and Medium Business owners

Industry/Entity Type

Business

Requirements
Must have
• *Details on all cards*

Company Name: Tallobrix Pty Ltd
ABN: 52 683 914 207
Address: 47-49 Pembury Street, Ashcombe Vale, Victoria 3172
Phone: 1300 GRAB UP
Fax: 03 9417 6258
Website: www.tallobrix.com.au
Logo/Handprint Icon

*Person Specific*

```html
<!DOCTYPE html>
<html lang="en">
<head>
<meta charset="utf-8">
<title>Tallobrix Business Card</title>
<link rel="stylesheet" href="https://fonts.googleapis.com/css2?family=Open+Sans:wght@400;600&display=swap">
<style>
  :root {
    --brand-blue: #3a7aab;
    --brand-blue-light: #4c8bbb;
    --paper: #ffffff;
    --ink: #333333;
    --ink-soft: #555555;
    --backdrop: #e6e6e4;
  }
  * { margin: 0; padding: 0; box-sizing: border-box; }
  html, body { width: 1200px; height: 900px; overflow: hidden; }
  body {
    background: var(--backdrop);
    font-family: "Open Sans", Arial, sans-serif;
    position: relative;
  }
  .card {
    position: absolute;
    width: 560px;
    height: 352px;
    overflow: hidden;
    box-shadow: 0 2px 6px rgba(0,0,0,0.15);
  }
  /* Front */
  .card-front {
    left: 60px;
    top: 100px;
    background: var(--brand-blue);
    color: var(--paper);
  }
  .card-front .pattern-area {
    position: absolute;
    left: 230px;
    top: 0;
    width: 330px;
    height: 352px;
    background: linear-gradient(135deg, var(--brand-blue) 0%, var(--brand-blue-light) 50%, var(--brand-blue) 100%);
  }
  .brand-name {
    position: absolute;
    left: 34px;
    top: 82px;
    font-size: 38px;
    font-weight: 400;
    letter-spacing: 1px;
    display: flex;
    align-items: center;
    gap: 10px;
  }
  .brand-dot {
    width: 14px;
    height: 14px;
    border-radius: 50%;
    background: var(--paper);
  }
  .company-name {
    position: absolute;
    left: 100px;
    top: 172px;
    font-size: 15px;
  }
  .details {
    position: absolute;
    left: 40px;
    font-size: 12.5px;
    line-height: 17px;
    display: grid;
    grid-template-columns: 60px auto;
  }
  .details-company { top: 208px; }
  .details-contact { top: 288px; grid-template-columns: 66px auto; }
  /* Back */
  .card-back {
    left: 580px;
    top: 470px;
    background: var(--paper);
    color: var(--ink);
  }
  .side-tab {
    position: absolute;
    left: 0;
    top: 122px;
    width: 58px;
    height: 150px;
    background: var(--brand-blue);
    border-radius: 0 12px 12px 0;
  }
  .corner-brand {
    position: absolute;
    right: 36px;
    top: 30px;
    display: flex;
    align-items: center;
    gap: 8px;
    color: var(--brand-blue);
    font-size: 20px;
    font-weight: 600;
  }
  .corner-brand .brand-dot { background: var(--brand-blue); width: 12px; height: 12px; }
  .person-name {
    position: absolute;
    left: 86px;
    top: 134px;
    font-size: 25px;
    font-weight: 600;
  }
  .person-role {
    position: absolute;
    left: 86px;
    top: 170px;
    font-size: 14px;
    color: var(--ink-soft);
  }
  .person-contact {
    position: absolute;
    left: 86px;
    top: 218px;
    font-size: 15px;
    line-height: 23px;
    color: var(--ink-soft);
    list-style: none;
  }
</style>
</head>
<body>
  <section class="card card-front">
    <div class="pattern-area" role="img" aria-label="Faint crossing diagonal line pattern"></div>
    <div class="brand-name"><span class="brand-dot"></span>Tallobrix</div>
    <p class="company-name">Tallobrix Pty Ltd</p>
    <dl class="details details-company">
      <dt>ABN:</dt><dd>52 683 914 207</dd>
      <dt>address:</dt><dd>47-49 Pembury Street,<br>Ashcombe Vale,<br>Victoria 3172</dd>
    </dl>
    <dl class="details details-contact">
      <dt>phone:</dt><dd>1300 GRAB UP</dd>
      <dt>fax:</dt><dd>03 9417 6258</dd>
    </dl>
  </section>

  <section class="card card-back">
    <div class="side-tab"></div>
    <div class="corner-brand"><span class="brand-dot"></span>Tallobrix</div>
    <h1 class="person-name">Martin Hale</h1>
    <p class="person-role">director</p>
    <ul class="person-contact">
      <li>(999) 999 999</li>
      <li>martin.hale@tallobrix.au</li>
      <li>www.tallobrix.com.au</li>
    </ul>
  </section>
</body>
</html>
```